Brightline Villas Estepona listings flyer

Brightline Villas Estepona are a specialist estate agency focussed solely on selling modern and contemporary homes.

We need an A4 folded flyer to be designed so that Brightline Villas Estepona can leaflet drop all of the modern homes for sale in our area to generate new instructions / listings. We need to engage with owners of those types of homes by posting this marketing material through their letter boxes in the hope that they see our funky and modern design and decide to call us about our services to sell their home, if for sale.

We would like to see sharp lines and a modern design (see our logo for style and colour scheme), with lots of white spaces and using photos which can blend in to the background to provide a powerful and impacting image to set us aside from any other direct mail leaflets which may be in their post box. It needs to show

* Quality
* Style
* Modern and forward thinking in design and outlook
* Professionalism

Front page
Top:
Logo of Brightline Villas Estepona.
Helping you sell your modern home. It’s all we do!

4 property photos in a grid position

Bottom banner
If you are thinking of selling, read on…

INSIDE LEFT & RIGHT (DOUBLE PAGE POSSIBLY BLANK WHITE BACKGROUND)
Title: Use Brightline Villas Estepona – the specialist modern homes agency to sell your home

We bring an exciting and dynamic mix of modern marketing with good old fashioned service to guarantee only the most qualified clients will be viewing your home (use online marketing image)

Marketing packages include stylish online brochures, professional photography, stunning drone video footage, informative video walk thru’s and unique floor plans (use drone and floor plan images)

Targeted social media campaigns focusing on international clientele actively looking to buy property in southern Spain (use social media image)

Bespoke, powerful advertising packages enable worldwide exposure for both online and traditional channels to market. We can be as discreet or as visible as you want us to be to sell your home

During our 20 years on the Costa del Sol, we have built up an enviable network of collaborating agents meaning you only have to instruct one expert real estate agent, Brightline Villas Estepona, to gain maximum exposure for your home

BACK PAGE

If you want service that matches the value of your home, contact us today for a private, personalised consultation. Brightline Villas Estepona. It’s all we do.

Suite 14
Torrenova Office Park
Calle Los Almendros
Valdemoro, Marbella

Tel: +34 952 418 306
Mobil y Whatsapp: +34 677 342 815
Email: info@brightlinevillasestepona.example
www.brightlinevillasestepona.example

Target Market(s)

Wealthy property owners of contemporary and modern homes who are looking to sell their home

Industry/Entity Type

Real Estate Agent

Font styles to use
Serif
Sans Serif

Colors
606060
e7e7e7
f5f5f5

Requirements
Must have
• Classy, professional, modern design with the ability to stand out from other leaflet drops / direct mail in letter box
Nice to have
• straight lines to border photos
• Maybe extend the lines further than they should so it has the look of an architects plan
• Blend in images to white background in the middle open double page
Should not have
• Lots of different colours

```html
<!DOCTYPE html>
<html lang="en">
<head>
<meta charset="utf-8">
<title>Brightline Villas Estepona – Flyer Outside</title>
<link href="https://fonts.googleapis.com/css2?family=Montserrat:wght@400;500;700;800&family=Open+Sans:ital,wght@0,400;0,600;1,400&display=swap" rel="stylesheet">
<style>
  :root{
    --ink:#3a3a3a;
    --grey:#606060;
    --mid:#8a8a8a;
    --line:#c4c4c4;
    --paper:#fbfbfb;
    --tint:#f5f5f5;
    --pale:#e7e7e7;
    --stage:#d9d9d9;
  }
  *{box-sizing:border-box;margin:0;padding:0}
  html,body{width:902px;height:1200px;overflow:hidden;background:var(--stage)}
  body{font-family:"Open Sans",Arial,sans-serif;color:var(--grey);position:relative}
  .spread{position:absolute;left:21px;top:299px;width:860px;height:602px;background:var(--paper);box-shadow:0 10px 24px rgba(0,0,0,.25);display:flex}
  .page{position:relative;width:430px;height:602px}
  .back-page{background:linear-gradient(90deg,var(--tint),var(--paper))}
  .front-page{background:var(--paper);border-left:1px solid #eee}

  .ghost-photo{position:absolute;left:0;top:0;width:215px;height:602px;background:linear-gradient(90deg,rgba(200,200,200,.45),rgba(240,240,240,.1))}

  .quote{position:absolute;left:52px;top:245px;width:340px;height:78px;border:1px solid var(--line);border-radius:8px;padding:8px 14px;text-align:center;font-style:italic;font-size:11.6px;line-height:16px;color:var(--ink);background:rgba(255,255,255,.35)}
  .quote-mark{position:absolute;font-family:"Montserrat",sans-serif;font-weight:800;font-size:40px;color:#bdbdbd;line-height:1}
  .quote-mark.open{left:-12px;top:-6px}
  .quote-mark.close{right:-16px;bottom:-30px}

  .brand{font-family:"Montserrat",sans-serif;font-weight:500;color:var(--ink);text-align:center;letter-spacing:.3px}
  .back-brand{position:absolute;left:0;width:430px;top:432px;font-size:12px}
  .brand-dot{display:inline-block;width:8px;height:8px;background:var(--ink);margin-right:6px;vertical-align:1px}

  .icons{position:absolute;top:462px;left:0;width:430px;display:flex;justify-content:center;gap:8px}
  .icons svg{width:12px;height:12px}

  .contact{position:absolute;left:0;width:430px;top:486px;text-align:center;font-size:9.6px;line-height:14.5px;color:var(--ink)}

  .front-brand{position:absolute;left:0;width:430px;top:98px;font-size:15px}
  .title{position:absolute;left:0;width:430px;top:150px;text-align:center;font-family:"Montserrat",sans-serif;color:var(--ink)}
  .title-main{font-weight:800;font-size:33px;line-height:36px;letter-spacing:.5px}
  .title-sub{font-weight:700;font-size:22px;letter-spacing:4px;line-height:26px}
  .tagline{position:absolute;left:0;width:430px;top:220px;text-align:center;font-family:"Montserrat",sans-serif;font-weight:500;font-size:14px;line-height:19px;color:var(--grey)}

  .frame{position:absolute;left:0;top:0;width:430px;height:602px;pointer-events:none}
  .gallery{position:absolute;left:0;top:268px;width:430px;height:224px}

  .read-on{position:absolute;left:0;width:430px;top:534px;text-align:center;font-family:"Montserrat",sans-serif;font-size:12px;color:var(--mid);letter-spacing:.3px}
  .front-url{position:absolute;left:0;width:430px;top:575px;text-align:center;font-size:9.6px;color:var(--ink)}
</style>
</head>
<body>
<main class="spread">
  <section class="page back-page">
    <div class="ghost-photo" role="img" aria-label="Faded photo of a white modern villa with terrace blending into the white background"></div>

    <blockquote class="quote">
      <span class="quote-mark open">“</span>
      If you want service that matches the value of<br>your home, contact us today for a private,<br>personalised consultation.<br>Brightline Villas Estepona. It’s all we do.
      <span class="quote-mark close">”</span>
    </blockquote>

    <div class="brand back-brand"><span class="brand-dot"></span>BRIGHTLINE VILLAS ESTEPONA</div>

    <div class="icons" aria-hidden="true">
      <svg viewBox="0 0 12 12"><circle cx="6" cy="6" r="6" fill="#3a3a3a"/><path d="M6 2.6a2 2 0 0 0-2 2c0 1.6 2 4.2 2 4.2s2-2.6 2-4.2a2 2 0 0 0-2-2z" fill="#fff"/><circle cx="6" cy="4.6" r=".7" fill="#3a3a3a"/></svg>
      <svg viewBox="0 0 12 12"><circle cx="6" cy="6" r="6" fill="#3a3a3a"/><path d="M4 3.2l1 .1.5 1.5-.7.6a4 4 0 0 0 1.8 1.8l.6-.7 1.5.5.1 1a1 1 0 0 1-1 .9A5 5 0 0 1 3.1 4.2a1 1 0 0 1 .9-1z" fill="#fff"/></svg>
      <svg viewBox="0 0 12 12"><circle cx="6" cy="6" r="6" fill="#3a3a3a"/><rect x="4.2" y="2.6" width="3.6" height="6.8" rx=".7" fill="#fff"/><rect x="4.8" y="3.4" width="2.4" height="4.6" fill="#3a3a3a"/></svg>
      <svg viewBox="0 0 12 12"><circle cx="6" cy="6" r="6" fill="#3a3a3a"/><rect x="3" y="4" width="6" height="4.2" fill="#fff"/><path d="M3 4l3 2.3L9 4" fill="none" stroke="#3a3a3a" stroke-width=".7"/></svg>
      <svg viewBox="0 0 12 12"><circle cx="6" cy="6" r="6" fill="#3a3a3a"/><circle cx="6" cy="6" r="3" fill="none" stroke="#fff" stroke-width=".8"/><path d="M3 6h6M6 3c-1.4 1.8-1.4 4.2 0 6M6 3c1.4 1.8 1.4 4.2 0 6" fill="none" stroke="#fff" stroke-width=".6"/></svg>
    </div>

    <address class="contact" style="font-style:normal">
      Suite 14 Torrenova Office Park<br>
      Calle Los Almendros Valdemoro, Marbella<br>
      +34 952 418 306<br>
      +34 677 342 815<br>
      info@brightlinevillasestepona.example<br>
      www.brightlinevillasestepona.example
    </address>
  </section>

  <section class="page front-page">
    <div class="brand front-brand"><span class="brand-dot"></span>BRIGHTLINE VILLAS</div>

    <h1 class="title">
      <div class="title-main">BRIGHTLINE</div>
      <div class="title-sub">VILLAS ESTEPONA</div>
    </h1>
    <p class="tagline">HELPING YOU SELL YOUR MODERN HOME.<br>IT’S ALL WE DO!</p>

    <svg class="frame" viewBox="0 0 430 602" aria-hidden="true">
      <g fill="none" stroke="#b5b5b5" stroke-width="1">
        <path d="M48 190 H30 V278"/>
        <path d="M382 190 H400 V278"/>
        <path d="M30 480 V542 H44"/>
        <path d="M400 480 V542 H386"/>
      </g>
    </svg>

    <svg class="gallery" viewBox="0 0 430 224">
      <defs>
        <linearGradient id="skyA" x1="0" y1="0" x2="0" y2="1"><stop offset="0" stop-color="#4f8fd8"/><stop offset=".55" stop-color="#eef1f4"/><stop offset="1" stop-color="#6aa64a"/></linearGradient>
        <linearGradient id="skyB" x1="0" y1="0" x2="0" y2="1"><stop offset="0" stop-color="#3f82d2"/><stop offset=".5" stop-color="#f2f2f2"/><stop offset="1" stop-color="#5f9a3f"/></linearGradient>
        <linearGradient id="skyC" x1="0" y1="0" x2="0" y2="1"><stop offset="0" stop-color="#2a6fc6"/><stop offset=".55" stop-color="#f0f0ee"/><stop offset="1" stop-color="#9a9384"/></linearGradient>
        <linearGradient id="skyD" x1="0" y1="0" x2="0" y2="1"><stop offset="0" stop-color="#4d8fd9"/><stop offset=".5" stop-color="#f4f2ec"/><stop offset="1" stop-color="#27a6df"/></linearGradient>
      </defs>
      <polygon points="0,0 190,0 224,108 0,108" fill="url(#skyA)" role="img" aria-label="Photo of a terraced white modern villa with lawn and pool"/>
      <polygon points="200,2 430,0 430,124 234,110" fill="url(#skyB)" role="img" aria-label="Photo of a cubic white modern house with garden"/>
      <polygon points="0,116 230,116 246,224 0,224" fill="url(#skyC)" role="img" aria-label="Photo of white villas with palm trees and patio"/>
      <polygon points="242,132 430,132 430,224 262,224" fill="url(#skyD)" role="img" aria-label="Photo of a modern pavilion house behind a blue swimming pool"/>
    </svg>

    <p class="read-on">IF YOU ARE THINKING OF SELLING, READ ON...</p>
    <p class="front-url">www.brightlinevillasestepona.example</p>
  </section>
</main>
</body>
</html>
```